Business Consultancy Business Card Design

Business Card design required for Business Analysis and Project Consultancy business based in Scotland.

Company Name - Brevick Advisory

Back - Company Logo

Front Details

Owen Brevick
07642 918 305
owen.brevick@brevickadvisory.com
http://www.brevickadvisory.com

Colours should match the logo colours but I am open to design ideas.

```html
<!DOCTYPE html>
<html lang="en">
<head>
<meta charset="utf-8">
<title>Brevick Advisory – Business Card</title>
<link rel="stylesheet" href="https://fonts.googleapis.com/css2?family=Roboto:wght@300;400&display=swap">
<style>
  :root {
    --blue: #1f9fdc;
    --green: #5cb833;
    --white: #ffffff;
    --ink: #5f6165;
    --ink-soft: #7a7c80;
    --backdrop: #e9eaec;
  }
  * { box-sizing: border-box; margin: 0; padding: 0; }
  html, body {
    width: 1200px; height: 873px; overflow: hidden;
    background: var(--backdrop);
    font-family: "Roboto", Arial, sans-serif;
  }
  .sheet {
    position: relative; width: 1200px; height: 873px;
    display: flex; align-items: center; justify-content: center; gap: 40px;
  }
  .card {
    position: relative; width: 540px; height: 309px;
    background: var(--white); overflow: hidden;
    box-shadow: 0 4px 14px rgba(0,0,0,.12);
  }

  /* front */
  .front .band-top { position: absolute; left: 0; top: 0; width: 100%; height: 26px; background: var(--blue); }
  .front .band-bottom { position: absolute; left: 0; bottom: 0; width: 100%; height: 46px; background: var(--green); }
  .brand-mark { position: absolute; left: 44px; top: 52px; display: flex; align-items: center; gap: 8px; }
  .brand-mark .dot { width: 14px; height: 14px; border-radius: 50%; background: var(--blue); }
  .brand-mark .name { font-size: 13px; font-weight: 400; color: var(--green); letter-spacing: .5px; }
  .person { position: absolute; left: 44px; top: 92px; }
  .person .name { font-size: 34px; font-weight: 300; color: var(--ink); line-height: 1; }
  .person .role { margin-top: 6px; font-size: 13px; font-weight: 300; color: var(--ink-soft); }
  .rule { position: absolute; height: 3px; }
  .rule-blue { left: 210px; top: 150px; width: 300px; background: var(--blue); }
  .rule-green { left: 120px; top: 238px; width: 250px; background: var(--green); }
  .contacts { position: absolute; left: 210px; top: 162px; list-style: none; }
  .contacts li { display: flex; align-items: center; gap: 12px; height: 22px; font-size: 12.5px; font-weight: 400; color: var(--ink); }
  .contacts svg { width: 14px; height: 14px; flex: none; }

  /* back */
  .back .band-top { position: absolute; left: 0; top: 0; width: 100%; height: 118px; background: var(--blue); }
  .back .band-bottom { position: absolute; left: 0; bottom: 0; width: 100%; height: 131px; background: var(--green); }
  .back .lockup { position: absolute; left: 40px; top: 118px; height: 60px; display: flex; align-items: center; gap: 14px; }
  .back .lockup .dot { width: 40px; height: 40px; border-radius: 50%; background: var(--blue); }
  .back .lockup .divider { width: 1.5px; height: 34px; background: var(--ink); }
  .back .lockup .name { font-size: 25px; font-weight: 400; color: var(--ink); letter-spacing: 1px; }
</style>
</head>
<body>
<main class="sheet">
  <section class="card front" aria-label="Card front">
    <div class="band-top"></div>
    <div class="band-bottom"></div>
    <div class="brand-mark"><span class="dot"></span><span class="name">Brevick Advisory</span></div>
    <div class="person">
      <h1 class="name">Owen Brevick</h1>
      <p class="role">Owner</p>
    </div>
    <div class="rule rule-blue"></div>
    <ul class="contacts">
      <li>
        <svg viewBox="0 0 14 14" aria-hidden="true"><rect x="4" y="1" width="6" height="12" rx="1.2" fill="#5f6165"/><rect x="5" y="2.5" width="4" height="6" fill="#fff"/></svg>
        07642 918 305
      </li>
      <li>
        <svg viewBox="0 0 14 14" aria-hidden="true"><rect x="1" y="3" width="12" height="8" fill="#5f6165"/><path d="M1 3 L7 8 L13 3 M1 11 L5.5 7 M13 11 L8.5 7" stroke="#fff" stroke-width="1" fill="none"/></svg>
        owen.brevick@brevickadvisory.com
      </li>
      <li>
        <svg viewBox="0 0 14 14" aria-hidden="true"><g fill="none" stroke="#5f6165" stroke-width="1"><circle cx="7" cy="7" r="5.5"/><ellipse cx="7" cy="7" rx="2.5" ry="5.5"/><path d="M1.5 7h11M2.5 4h9M2.5 10h9"/></g></svg>
        http://www.brevickadvisory.com
      </li>
    </ul>
    <div class="rule rule-green"></div>
  </section>

  <section class="card back" aria-label="Card back">
    <div class="band-top"></div>
    <div class="band-bottom"></div>
    <div class="lockup"><span class="dot"></span><span class="divider"></span><span class="name">BREVICK ADVISORY</span></div>
  </section>
</main>
</body>
</html>
```